Business Card - Business Consultancy

Newly Established Company, specializing in Business Consultancy, Human Resource Management, Talent Acquisition and Payroll Solutions.

We need a Business card design which portrays "elegance" and a very sleek yet business-like design. We would like a nice blue trimming (which goes well with the logo) to separate the content of the business card at the top. We would also like to see the design using the color silver either as a background or incorporated into it.

The final design should be a Business card which has colors matching the logo; a nice font; the above-mentioned specifics that adheres to the theme of "a stylish and professional business"

FYI: please do not have too fanciful designs.

Industry/Entity Type

Business Consultant

Contact Information for Business Card

Darren Loh
Business Development Director
Opal Staffing Advisory Private Limited
27 Marlow Street, #05-03B
Crescent Harbour Tower
Singapore 061732
Mobile : (+65) 93584617
Email : dloh@opalstaffing-advisory.com
Alternative : opalstaffingadvisory@mailvista.com

Requirements
Must have
• Nice Blue Trimming matching Logo which separates content, see attached
• Design incorporates either a silver background or the use of the color silver
Should not have
• No Fanciful Designs
• No Childish Designs
• No Overly Complicated Designs

```html
<!DOCTYPE html>
<html lang="en">
<head>
<meta charset="utf-8">
<title>Opal Staffing Advisory – Business Card</title>
<link rel="stylesheet" href="https://fonts.googleapis.com/css2?family=Arimo:wght@400;700&family=Roboto+Condensed:wght@700&display=swap">
<style>
  :root {
    --backdrop: #d9dadc;
    --card: #ffffff;
    --ink: #111111;
    --muted: #6b6b6b;
    --brand-blue: #1483d4;
    --brand-green: #7cc242;
    --silver: #b9bcc0;
  }
  * { box-sizing: border-box; margin: 0; padding: 0; }
  html, body {
    width: 1200px; height: 960px; overflow: hidden;
    background: radial-gradient(circle at 50% 40%, #eceded 0%, var(--backdrop) 70%);
    font-family: "Arimo", Arial, sans-serif;
    color: var(--ink);
  }
  .sheet {
    width: 1200px; height: 960px;
    display: flex; flex-direction: column; align-items: center; justify-content: center;
    gap: 60px;
  }
  .card {
    position: relative;
    width: 595px; height: 340px;
    background: var(--card);
    box-shadow: 0 10px 26px rgba(0,0,0,0.18);
    overflow: hidden;
  }

  /* Brand lockup */
  .brand { display: flex; align-items: center; gap: 16px; }
  .brand-dot { border-radius: 50%; background: var(--brand-blue); flex: none; }
  .brand-name { font-weight: 700; color: var(--ink); line-height: 1.05; }

  /* Front */
  .card-front { display: flex; flex-direction: column; align-items: center; justify-content: center; gap: 34px; }
  .card-front .brand-dot { width: 74px; height: 74px; }
  .card-front .brand-name { font-size: 38px; }
  .services {
    font-family: "Roboto Condensed", "Arial Narrow", sans-serif;
    font-weight: 700; font-size: 19px; letter-spacing: 0.2px;
  }
  .front-rule {
    position: absolute; left: 0; right: 0; bottom: 0; height: 8px;
    background: linear-gradient(90deg, var(--brand-blue), var(--silver));
  }

  /* Back */
  .card-back { padding: 34px 36px; }
  .back-head { display: flex; align-items: center; }
  .card-back .brand-dot { width: 46px; height: 46px; }
  .card-back .brand-name { font-size: 20px; width: 150px; }
  .divider { width: 1px; height: 90px; background: var(--silver); margin: 0 30px; }
  .person { margin-left: auto; text-align: right; }
  .person-name { font-size: 30px; font-weight: 700; }
  .person-title { font-size: 15px; color: var(--muted); margin-top: 6px; }

  .address {
    position: absolute; left: 36px; top: 150px;
    font-size: 14px; line-height: 1.35;
  }
  .address .company { font-weight: 700; }

  .contacts {
    position: absolute; right: 36px; bottom: 30px;
    list-style: none; font-size: 15px;
  }
  .contacts li { display: flex; align-items: center; justify-content: flex-end; gap: 10px; margin-top: 7px; }
  .icon {
    width: 24px; height: 24px; border-radius: 50%;
    background: var(--brand-blue); display: grid; place-items: center;
  }
  .back-rule {
    position: absolute; left: 0; top: 0; bottom: 0; width: 8px;
    background: linear-gradient(180deg, var(--brand-blue), var(--silver));
  }
</style>
</head>
<body>
<main class="sheet">

  <section class="card card-front" aria-label="Card front">
    <div class="brand">
      <span class="brand-dot"></span>
      <span class="brand-name">Opal Staffing<br>Advisory</span>
    </div>
    <p class="services">Recruitment | HR Solutions | Business Consultancy</p>
    <span class="front-rule"></span>
  </section>

  <section class="card card-back" aria-label="Card back">
    <span class="back-rule"></span>
    <header class="back-head">
      <div class="brand">
        <span class="brand-dot"></span>
        <span class="brand-name">Opal Staffing Advisory</span>
      </div>
      <span class="divider"></span>
      <div class="person">
        <p class="person-name">Darren Loh</p>
        <p class="person-title">Business Development Director</p>
      </div>
    </header>

    <address class="address" style="font-style:normal">
      <span class="company">Opal Staffing Advisory Pte. Ltd.</span><br>
      27 Marlow Street, #05-03B<br>
      Crescent Harbour Tower<br>
      Singapore 061732
    </address>

    <ul class="contacts">
      <li>+65 9358-4617
        <span class="icon"><svg width="12" height="14" viewBox="0 0 12 14"><rect x="2" y="0.8" width="8" height="12.4" rx="1.5" fill="none" stroke="#fff" stroke-width="1.4"/><circle cx="6" cy="10.8" r="0.9" fill="#fff"/></svg></span>
      </li>
      <li>dloh@opalstaffing-advisory.com
        <span class="icon"><svg width="14" height="10" viewBox="0 0 14 10"><rect x="0.7" y="0.7" width="12.6" height="8.6" rx="1" fill="none" stroke="#fff" stroke-width="1.3"/><path d="M1 1.2 7 6 13 1.2" fill="none" stroke="#fff" stroke-width="1.3"/></svg></span>
      </li>
      <li>opalstaffingadvisory@mailvista.com
        <span class="icon"><svg width="14" height="10" viewBox="0 0 14 10"><rect x="0.7" y="0.7" width="12.6" height="8.6" rx="1" fill="none" stroke="#fff" stroke-width="1.3"/><path d="M1 1.2 7 6 13 1.2" fill="none" stroke="#fff" stroke-width="1.3"/></svg></span>
      </li>
    </ul>
  </section>

</main>
</body>
</html>
```